Home page web design for "Tales from Thee"

We need a home page web design for a start up company that will write memoirs for seniors.
The completed project will need to include PSD files...NO HTML or CSS necessary.
Attached is a brief outline concept that may give you some ideas...but you are the creative professionals, so please feel free to add your ideas. We will also attach some files that show you our logo, brochures, and photos that could be used to give you ideas of our focus.
There will need to be access to the other pages on the home page to include: 'About Us'; 'How We Can Help'; 'Community Sessions'; 'Senior Consulting ' and 'Contact Us'.
Updates

Target Market(s)

Seniors and Baby Boomers

Industry/Entity Type

It Company

Number of Pages Required

1 page

Colors
f9ba93
fbca95
faa54b
faf289
f37123

Requirements
Must have
• Script easy on senior eyes.
• Initial contact number would be 844-4LANTERN
Nice to have
• While the color pallet is non-specific we prefer the warm colors.
• salmon, peach.......
• NOT so much the orange of Halloween:)
• However, please utilize your creativity and put in colors you feel will draw best with your design.

```html
<!DOCTYPE html>
<html lang="en">
<head>
<meta charset="utf-8">
<title>Tales from Thee — Home</title>
<link rel="stylesheet" href="https://fonts.googleapis.com/css2?family=Bitter:wght@400;700&family=Lato:wght@400;700&family=Roboto:wght@400;500&display=swap">
<style>
  :root {
    --cream: #fdfbeb;
    --peach-band: #f9d7c0;
    --orange: #faa54b;
    --orange-light: #fbbb6e;
    --yellow: #f8ef92;
    --gold: #c9a24a;
    --ink: #222222;
    --body-ink: #3a3a2e;
    --dark: #333333;
    --footer-ink: #e6e6e6;
    --footer-muted: #9a9a9a;
    --white: #ffffff;
  }
  * { box-sizing: border-box; margin: 0; padding: 0; }
  html, body { width: 958px; height: 1200px; overflow: hidden; }
  body { position: relative; background: var(--cream); font-family: "Lato", sans-serif; color: var(--ink); }

  .site-header { position: absolute; left: 0; top: 0; width: 958px; height: 132px; background: var(--cream); }
  .header-panel { position: absolute; left: 110px; top: 0; width: 738px; height: 138px; background: #fffef6; box-shadow: 0 0 10px rgba(0,0,0,.12); }
  .brand { position: absolute; left: 125px; top: 22px; display: flex; align-items: center; gap: 10px; }
  .brand-mark { width: 18px; height: 18px; border-radius: 50%; background: var(--gold); }
  .brand-name { font-family: "Bitter", serif; font-size: 26px; font-weight: 400; color: var(--gold); }

  .call-box { position: absolute; left: 699px; top: 28px; display: flex; align-items: center; gap: 8px; }
  .call-icon { width: 28px; height: 28px; }
  .call-label { font-size: 11px; font-weight: 700; letter-spacing: 1.5px; color: #555; }
  .call-number { font-size: 17px; font-weight: 400; color: #333; line-height: 1.1; }

  .peach-band { position: absolute; left: 0; top: 132px; width: 958px; height: 240px; background: var(--peach-band); }

  .main-nav { position: absolute; left: 60px; top: 96px; width: 836px; height: 42px; background: var(--orange); box-shadow: 0 3px 5px rgba(0,0,0,.18); }
  .main-nav ul { position: absolute; left: 50px; top: 0; width: 738px; height: 42px; list-style: none; display: flex; align-items: center; background: var(--orange-light); padding-left: 12px; }
  .main-nav li { font-size: 13.5px; color: var(--white); padding: 0 12px; border-left: 1px solid rgba(255,255,255,.35); white-space: nowrap; }
  .main-nav li:first-child { border-left: 0; color: var(--ink); }

  .hero { position: absolute; left: 110px; top: 138px; width: 738px; height: 234px; background: linear-gradient(100deg, #5a5a5a 0%, #9a9a9a 35%, #c8c8c8 60%, #6e6e6e 100%); overflow: hidden; }
  .hero-caption { position: absolute; left: 18px; top: 100px; font-family: "Bitter", serif; font-size: 21px; line-height: 29px; color: var(--white); }
  .hero-dots { position: absolute; left: 18px; top: 206px; display: flex; gap: 9px; }
  .hero-dots span { width: 8px; height: 8px; border-radius: 50%; background: var(--white); }
  .hero-dots span:first-child { background: var(--orange); }

  .content { position: absolute; left: 0; top: 372px; width: 958px; height: 760px; background: var(--yellow); }
  .corner-ornament { position: absolute; width: 70px; height: 70px; background: #eedb7c; opacity: .5; border-radius: 4px; }
  .corner-ornament.top-left { left: 82px; top: 12px; }
  .corner-ornament.bottom-right { left: 795px; top: 633px; }

  .lead { position: absolute; left: 110px; width: 700px; font-family: "Roboto", sans-serif; font-weight: 500; font-size: 16px; line-height: 21px; color: var(--ink); }
  .lead.question { top: 62px; }
  .lead.promise { top: 100px; width: 665px; }

  .story-block { position: absolute; left: 110px; width: 352px; font-family: "Lato", sans-serif; font-size: 12.5px; line-height: 21.5px; color: var(--body-ink); }
  .story-block.intro { top: 154px; }
  .story-block.heritage { top: 235px; }
  .story-block.genealogy { top: 385px; }
  .story-block.prompt { top: 550px; line-height: 16px; }
  .story-block.prompt p { margin-bottom: 7px; }

  .actions { position: absolute; left: 154px; top: 670px; display: flex; gap: 25px; }
  .btn { width: 112px; height: 29px; background: var(--dark); color: var(--white); font-family: "Roboto", sans-serif; font-size: 12.5px; display: flex; align-items: center; justify-content: center; box-shadow: 0 2px 3px rgba(0,0,0,.25); }
  .btn.learn { width: 109px; }

  .photo { position: absolute; border: 6px solid var(--white); box-shadow: 0 2px 6px rgba(0,0,0,.25); }
  .photo.one   { left: 472px; top: 171px; width: 178px; height: 107px; transform: rotate(-2deg); background: linear-gradient(135deg, #3b3f2c, #6f7160 50%, #2b2d22); }
  .photo.two   { left: 667px; top: 171px; width: 176px; height: 105px; transform: rotate(1.5deg); background: linear-gradient(180deg, #d7dfe6, #a7b8c6 55%, #8c7d6c); }
  .photo.three { left: 562px; top: 265px; width: 178px; height: 105px; transform: rotate(1deg); background: linear-gradient(135deg, #3a2216, #8a5a3a 50%, #2a180f); }
  .photo.four  { left: 470px; top: 418px; width: 180px; height: 106px; transform: rotate(-2deg); background: linear-gradient(135deg, #7aa44a, #b7c790 55%, #5f7f38); }
  .photo.five  { left: 665px; top: 415px; width: 180px; height: 103px; transform: rotate(1deg); background: linear-gradient(135deg, #e9ecef, #9bb0c8 50%, #3d5a80); }
  .photo.six   { left: 564px; top: 518px; width: 178px; height: 97px; transform: rotate(1deg); background: linear-gradient(180deg, #efefef, #c9b7a8 55%, #6d6a78); }

  .site-footer { position: absolute; left: 0; top: 1132px; width: 958px; height: 68px; background: var(--dark); text-align: center; }
  .footer-nav { margin-top: 10px; font-family: "Roboto", sans-serif; font-size: 10px; color: var(--footer-ink); }
  .footer-nav span { padding: 0 5px; }
  .footer-nav .sep { padding: 0; color: var(--footer-muted); }
  .copyright { margin-top: 6px; font-family: "Roboto", sans-serif; font-size: 9.5px; color: var(--footer-muted); }
  .footer-rule { width: 280px; height: 1px; margin: 8px auto 0; background: #4a4a4a; }
</style>
</head>
<body>
  <header class="site-header">
    <div class="header-panel"></div>
    <div class="brand">
      <span class="brand-mark"></span>
      <span class="brand-name">Tales from Thee</span>
    </div>
    <div class="call-box">
      <svg class="call-icon" viewBox="0 0 28 28" aria-hidden="true">
        <circle cx="14" cy="14" r="12.5" fill="none" stroke="#f0a24f" stroke-width="1.5"/>
        <path d="M10 8.5c.8-.6 1.6-.4 2 .4l1 2c.3.6.1 1.2-.4 1.6l-.8.6c.6 1.5 1.7 2.7 3.2 3.4l.6-.8c.4-.5 1-.7 1.6-.4l2 1c.8.4 1 1.2.4 2-.9 1.2-2.2 1.6-3.6 1-3.2-1.3-5.7-3.8-6.9-7-.5-1.4 0-2.8.9-3.8z" fill="#f0a24f"/>
      </svg>
      <div>
        <div class="call-label">CALL US TODAY</div>
        <div class="call-number">844-4LANTERN</div>
      </div>
    </div>
  </header>

  <div class="peach-band"></div>

  <nav class="main-nav">
    <ul>
      <li>HOME</li>
      <li>ABOUT US</li>
      <li>HOW WE CAN HELP</li>
      <li>COMMUNITY SERVICES</li>
      <li>SENIOR CONSULTING</li>
      <li>CONTACT US</li>
    </ul>
  </nav>

  <section class="hero" role="img" aria-label="Black and white photo of a grandfather reading a book with a young child">
    <p class="hero-caption">Every Life Legacy is a<br>Gift to Be Treasured<br>by the next generation</p>
    <div class="hero-dots"><span></span><span></span><span></span><span></span></div>
  </section>

  <main class="content">
    <div class="corner-ornament top-left" role="img" aria-label="Decorative corner flourish"></div>
    <div class="corner-ornament bottom-right" role="img" aria-label="Decorative corner flourish"></div>

    <h1 class="lead question">If You Were Alive In 100 Years, What Would You Share With Your Descendants?</h1>
    <h2 class="lead promise">Now You Have A Vehicle To Help You Immortalize Your Thoughts For The Future...specifically For Those Who Will Want To Know!</h2>

    <p class="story-block intro">We are not all presidents of countries or CEO's of fortune 500 companies! But "every life legacy is a gift to be treasured by the next generation."</p>
    <p class="story-block heritage">Does your family host generations of soldiers, doctors, farmers, scientists, mechanics, entrepreneurs, writers, politicians, contractors, pastors, artisans, athletes, musicians, etc..? Generational patterns can often emerge when writing your story that will interest the next generation.</p>
    <p class="story-block genealogy">A genealogy, while very relevant, doesn't offer the personal story of the names we find. A biography can place a deeper relevance on the face for future descendants. Every life is a legacy to pass forward and we at Tales from Thee believe everyone should chronicle their life journey in writing. This commitment allows you to be remembered for who you truly are as a person.</p>
    <div class="story-block prompt">
      <p>Think about it....</p>
      <p>Do you know the triumphs and tribulations of your ancestors?</p>
      <p>Do you wish you did?</p>
      <p>Well, so will those falling into your personal family tree.</p>
    </div>

    <div class="actions">
      <span class="btn gift">GREAT GIFT IDEA</span>
      <span class="btn learn">LEARN MORE</span>
    </div>

    <div class="photo one" role="img" aria-label="Photo of an elderly man holding a framed picture"></div>
    <div class="photo two" role="img" aria-label="Photo of an older couple walking by the sea"></div>
    <div class="photo three" role="img" aria-label="Photo of a warm candlelit room with old keepsakes"></div>
    <div class="photo four" role="img" aria-label="Photo of two hands clasped against green grass"></div>
    <div class="photo five" role="img" aria-label="Photo of a grandfather with a baby reading a book"></div>
    <div class="photo six" role="img" aria-label="Group photo of smiling seniors"></div>
  </main>

  <footer class="site-footer">
    <div class="footer-nav">
      <span>Home</span><span class="sep">|</span><span>About Us</span><span class="sep">|</span><span>How We can Help</span><span class="sep">|</span><span>Community Services</span><span class="sep">|</span><span>Senior Consulting</span><span class="sep">|</span><span>Contact Us</span>
    </div>
    <div class="copyright">© Copyright 2014 TalesfromThee. All Rights Reserved.</div>
    <div class="footer-rule"></div>
  </footer>
</body>
</html>
```